Very new and innovative Web design for Property managers of Vacation rentals

We are looking for a new website design for travel agencies and property managers specialised on vacation rentals business, holiday villas and apartments.

The end users of this website are travellers who are looking for a vacation home for their next holiday: this is the reason why the website must be easy to use, attractive, professional, possibly elegant and focused on get new reservations.

This is a draft of our current website: https://demo5.lunquora.com/
Please consider that we would like to have proposals with a totally different and innovative layout, surprise us!

These are the pages of the website:
• Homepage: feel free to redesign all the homepage as you wish, surprise us with something very new! Please consider that Property manager/Travel agencies usually want to have the opportunity to put in evidence groups of houses with specific characteristics (eg. villas with private swimming pool, apartment in big/small towns, villas with air co, etc…), destinations and tourist areas, and sometimes experiences or activities (please consider that the website layout must be suitable even if some of the previous sections are not used).
• Search page: we’d like to organise the results of the search page in three different ways:
o Grid
o Map
o List
• Property page: to illustrate the characteristics, descriptions, images, …. of the property. It is very important to put in evidence images of the property and to maintain the booking form (and the other call to action bottom – eg. whatsapp) always visible
• Custom pages: static pages composed usually by text, images and call to actions
• Contact us (general form)
• Info request (specific of a property form)
• Booking process
• Blog, organised in four pages:
o Home Page – introduction to the blog
o List of articles
o Single article
o Site Map (presentation of categories and sub-categories)

If possible, we’d prefer to receive the material in Adobe XD or similar so that we can obtain the three versions:
- smartphone
- tablet
- desktop

The website will be then developed in Bootstrap: as a result we’ll need the icons in SVG format (or the library used)

In attachment you can find the map of the website pages

```html
<!DOCTYPE html>
<html lang="en">
<head>
<meta charset="utf-8">
<title>StayLune – Exclusive Villas in Italy</title>
<link href="https://fonts.googleapis.com/css2?family=Mulish:wght@300;400;500;600;700;800&display=swap" rel="stylesheet">
<style>
:root{
  --green:#23aa6d;
  --ink:#2b2b2b;
  --text:#4a4a4a;
  --muted:#6b6b6b;
  --light-bg:#f3f3f3;
  --line:#e2e2e2;
  --footer:#1d1d1d;
  --white:#ffffff;
}
*{box-sizing:border-box;margin:0;padding:0}
html,body{width:1200px;height:3695px;overflow:hidden}
body{position:relative;font-family:"Mulish",sans-serif;color:var(--text);background:var(--white)}
.abs{position:absolute}
.btn{position:absolute;display:flex;align-items:center;justify-content:center;background:var(--green);color:var(--white);border-radius:40px;font-weight:700;text-decoration:none}

/* hero */
.hero{position:absolute;left:0;top:0;width:1200px;height:803px;background:linear-gradient(180deg,#2a3560 0%,#4a4a6a 25%,#8a6a4a 48%,#6a5240 62%,#2a3550 80%,#1c2a40 100%)}
.logo{position:absolute;display:flex;align-items:center;gap:12px;color:var(--white);font-size:40px;font-weight:500;letter-spacing:.3px}
.logo .dot{width:50px;height:50px;border-radius:50%;background:var(--white)}
.main-nav{position:absolute;top:72px;right:110px;display:flex;gap:35px}
.main-nav a{color:var(--white);font-size:16px;font-weight:600;text-decoration:none}
.hero-title{position:absolute;top:455px;left:0;width:1200px;text-align:center;color:var(--white);font-size:64px;font-weight:700;letter-spacing:.5px}
.search-panel{position:absolute;left:136px;top:553px;width:927px;height:127px;background:rgba(20,22,34,.72);border-radius:4px}
.field{position:absolute;top:31px;width:212px;height:38px;background:var(--white);border-radius:2px;display:flex;align-items:center;justify-content:space-between;padding:0 12px;font-size:14px;color:var(--muted)}
.search-btn{left:503px;top:651px;width:192px;height:54px;font-size:20px;gap:8px}

/* about */
.about-kicker{left:112px;top:915px;font-size:37px;font-weight:300;color:var(--ink)}
.about-title{left:112px;top:963px;font-size:39px;font-weight:700;color:var(--ink)}
.about-text{left:112px;top:1030px;width:346px;font-size:12.6px;line-height:27.3px;text-align:justify;color:var(--ink);letter-spacing:-.1px}
.photo{position:absolute}

/* rentals */
.rentals{position:absolute;left:0;top:1438px;width:1200px;height:717px;background:var(--light-bg)}
.section-title{position:absolute;left:0;width:1200px;text-align:center;font-size:38px;font-weight:600;color:var(--ink)}
.section-title em{font-style:normal;color:var(--green)}
.rule{position:absolute;left:568px;width:64px;height:3px;background:var(--green)}
.villa-card{position:absolute;top:1579px;width:270px;height:519px;background:var(--white);border:1px solid var(--line)}
.villa-name{position:absolute;left:21px;top:263px;font-size:19px;font-weight:700;color:var(--ink)}
.villa-rule{position:absolute;left:21px;top:300px;width:40px;height:3px;background:var(--green)}
.specs{position:absolute;left:21px;top:318px;width:230px;font-size:14px;color:var(--ink)}
.specs div{display:flex;justify-content:space-between;height:28.3px}
.specs span:last-child{width:52px}
.detail-btn{left:21px;top:446px;width:134px;height:46px;font-size:14px}

/* banner */
.banner{position:absolute;left:0;top:2155px;width:1200px;height:535px;background:linear-gradient(90deg,#7fa8d4 0%,#a9c3dc 40%,#b8c6d2 62%,#7a7a80 80%,#55555c 100%)}
.banner-line{position:absolute;left:112px;font-size:36px;color:var(--ink);font-weight:400;letter-spacing:.3px}
.banner-line.strong{color:var(--green);font-weight:800}
.offer-btn{left:112px;top:2413px;width:195px;height:64px;font-size:18px}

/* blog */
.blog-photo{position:absolute;top:2831px;width:314px;height:278px}
.blog-card{position:absolute;top:3054px;width:282px;height:216px;background:var(--white);border:1px solid var(--line);text-align:center;padding:0 22px}
.blog-date{margin-top:30px;font-size:15px;font-weight:600;color:var(--green)}
.blog-head{margin-top:10px;font-size:18px;font-weight:700;line-height:25px;color:var(--ink)}
.blog-text{margin-top:8px;font-family:Arial,sans-serif;font-size:13.5px;line-height:26px;color:var(--muted)}

/* footer */
.footer{position:absolute;left:0;top:3334px;width:1200px;height:361px;background:var(--footer)}
.contact{position:absolute;top:3371px;width:300px;text-align:center;color:var(--white)}
.contact .ring{width:66px;height:66px;margin:0 auto;border:2px solid var(--white);border-radius:50%;display:flex;align-items:center;justify-content:center}
.contact h4{margin-top:22px;font-size:17px;font-weight:700;letter-spacing:.5px}
.contact p{margin-top:6px;font-family:Arial,sans-serif;font-size:12.5px;line-height:23px;color:#cfcfcf}
.foot-nav{position:absolute;top:3585px;right:110px;display:flex;gap:32px}
.foot-nav a{color:var(--white);font-size:16px;font-weight:600;text-decoration:none}
.copyright{position:absolute;left:491px;top:3641px;font-size:13px;color:var(--white)}
</style>
</head>
<body>

<header class="hero" role="img" aria-label="Photo of a luxury villa with pool at dusk">
  <div class="logo" style="left:112px;top:52px"><span class="dot"></span>StayLune</div>
  <nav class="main-nav"><a href="#">Home</a><a href="#">Last Minute</a><a href="#">Special Offers</a><a href="#">Experience</a><a href="#">Blog</a><a href="#">Contact Us</a></nav>
  <h1 class="hero-title">Exclusive Villas in Italy</h1>
  <form class="search-panel">
    <div class="field" style="left:20px">Destination
      <svg width="10" height="14" viewBox="0 0 10 14"><path d="M5 0a5 5 0 0 0-5 5c0 4 5 9 5 9s5-5 5-9a5 5 0 0 0-5-5zm0 7a2 2 0 1 1 0-4 2 2 0 0 1 0 4z" fill="#555"/></svg></div>
    <div class="field" style="left:245px">Check In
      <svg width="13" height="13" viewBox="0 0 13 13"><rect x="1" y="2" width="11" height="10" fill="none" stroke="#555" stroke-width="1.4"/><path d="M1 5h11M4 0v3M9 0v3" stroke="#555" stroke-width="1.4"/></svg></div>
    <div class="field" style="left:469px">Check Out
      <svg width="13" height="13" viewBox="0 0 13 13"><rect x="1" y="2" width="11" height="10" fill="none" stroke="#555" stroke-width="1.4"/><path d="M1 5h11M4 0v3M9 0v3" stroke="#555" stroke-width="1.4"/></svg></div>
    <div class="field" style="left:693px">Travelers
      <svg width="10" height="6" viewBox="0 0 10 6"><path d="M0 0h10L5 6z" fill="#555"/></svg></div>
  </form>
  <a class="btn search-btn" href="#">Search
    <svg width="15" height="15" viewBox="0 0 15 15"><circle cx="6" cy="6" r="4.5" fill="none" stroke="#fff" stroke-width="2"/><path d="M9.5 9.5 14 14" stroke="#fff" stroke-width="2"/></svg></a>
</header>

<section>
  <h2 class="abs about-kicker">Looking for an</h2>
  <h2 class="abs about-title">Exclusive Holiday?</h2>
  <p class="abs about-text">Browse our vacation rental selections If you are looking for a real experiences, our portal is the right solution.Our vacation homes are all located in Italy and we take care of them and their owners at every time. Our goal is give to our guest authentic taste of holiday and our country.Our team is always ready to assure the best time and take care of you!Add a local experience to your stay with us: by diving into our local "network" you can have the unique chance to discover and travel our culture through the eye of a local...!</p>
  <a class="btn" href="#" style="left:112px;top:1329px;width:178px;height:56px;font-size:18px">View More</a>
  <div class="photo" role="img" aria-label="Villa with blue pool under a sunny sky" style="left:493px;top:925px;width:290px;height:208px;background:linear-gradient(180deg,#4f8fd6 0%,#b9c9d0 45%,#b5a890 65%,#2f8fd4 100%)"></div>
  <div class="photo" role="img" aria-label="Modern house lit at dusk" style="left:787px;top:885px;width:301px;height:248px;background:linear-gradient(180deg,#6a5a9a 0%,#8a6a8a 45%,#5a3a30 75%,#2a1e22 100%)"></div>
  <div class="photo" role="img" aria-label="Cooking fresh food in a kitchen" style="left:559px;top:1137px;width:290px;height:208px;background:linear-gradient(135deg,#3a3a30 0%,#6a5a4a 45%,#a08060 70%,#4a4030 100%)"></div>
  <div class="photo" role="img" aria-label="Red wine poured into glasses" style="left:853px;top:1137px;width:235px;height:208px;background:linear-gradient(135deg,#6a5048 0%,#9a3a3a 45%,#c8a8a0 70%,#7a4a44 100%)"></div>
</section>

<section class="rentals"></section>
<h2 class="section-title" style="top:1485px">New <em>Villas &amp; Vacation</em> Rentals</h2>
<div class="rule" style="top:1543px"></div>

<article class="villa-card" style="left:152px">
  <div class="photo" role="img" aria-label="Modern villa with palm trees and pool" style="left:-41px;top:26px;width:293px;height:215px;background:linear-gradient(180deg,#9ab8d8 0%,#d0d4d0 45%,#6a6050 65%,#2a9ac8 100%)"></div>
  <h3 class="villa-name">Residenza Lavreno</h3><div class="villa-rule"></div>
  <div class="specs"><div><span>Sleeps</span><span>15</span></div><div><span>Bedrooms</span><span>7</span></div><div><span>Bathrooms</span><span>5</span></div><div><span>Floor Area</span><span>300 m2</span></div></div>
  <a class="btn detail-btn" href="#">View Details</a>
</article>
<article class="villa-card" style="left:485px">
  <div class="photo" role="img" aria-label="Seaside villa with garden and pool" style="left:-41px;top:26px;width:293px;height:215px;background:linear-gradient(180deg,#6a8ab0 0%,#a8b4c0 35%,#7a6a5a 60%,#c0b8a8 85%,#4aa0c8 100%)"></div>
  <h3 class="villa-name">Villa Ortensa</h3><div class="villa-rule"></div>
  <div class="specs"><div><span>Sleeps</span><span>15</span></div><div><span>Bedrooms</span><span>7</span></div><div><span>Bathrooms</span><span>5</span></div><div><span>Floor Area</span><span>300 m2</span></div></div>
  <a class="btn detail-btn" href="#">View Details</a>
</article>
<article class="villa-card" style="left:817px">
  <div class="photo" role="img" aria-label="Countryside pool with sun loungers and trees" style="left:-41px;top:26px;width:293px;height:215px;background:linear-gradient(180deg,#3a5a30 0%,#5a7a40 40%,#4a8ab8 70%,#8a7a6a 100%)"></div>
  <h3 class="villa-name">Podere Calvisto</h3><div class="villa-rule"></div>
  <div class="specs"><div><span>Sleeps</span><span>15</span></div><div><span>Bedrooms</span><span>7</span></div><div><span>Bathrooms</span><span>5</span></div><div><span>Floor Area</span><span>300 m2</span></div></div>
  <a class="btn detail-btn" href="#">View Details</a>
</article>

<section class="banner" role="img" aria-label="Seafront villa terrace with infinity pool"></section>
<p class="banner-line" style="top:2236px">SED UT PERSPICIATIS</p>
<p class="banner-line strong" style="top:2285px">OMNIS ISTE NATUS ERROR SIT</p>
<p class="banner-line" style="top:2342px;font-size:31px">VOLUPTATEM ACCUSANTIUM LAUDANTIUM</p>
<a class="btn offer-btn" href="#">View Special Offer</a>

<h2 class="section-title" style="top:2737px">Latest <em>Blog</em></h2>
<div class="rule" style="top:2795px"></div>

<div class="blog-photo" role="img" aria-label="Yellow villa with long pool" style="left:112px;background:linear-gradient(180deg,#3a7ad0 0%,#6a9a50 40%,#c8b060 60%,#1a5ad0 100%)"></div>
<div class="blog-photo" role="img" aria-label="Stone farmhouse among trees" style="left:443px;background:linear-gradient(180deg,#5aa0e0 0%,#5a8a40 35%,#8a7058 60%,#5a7a3a 100%)"></div>
<div class="blog-photo" role="img" aria-label="Pool with gazebo in green hills" style="left:774px;background:linear-gradient(180deg,#5a9ae0 0%,#90b8e0 30%,#4a7a30 55%,#3aa0d8 75%,#8a8a7a 100%)"></div>

<article class="blog-card" style="left:129px"><p class="blog-date">OCTOBER 14, 2021</p><h3 class="blog-head">Sed ut perspiciatis unde omnis iste natus</h3><p class="blog-text">Nemo enim ipsam voluptatem quia voluptas sit aspernatur aut odit aut ratione voluptatem sequi</p></article>
<article class="blog-card" style="left:460px"><p class="blog-date">OCTOBER 14, 2021</p><h3 class="blog-head">Sed ut perspiciatis unde omnis iste natus</h3><p class="blog-text">Nemo enim ipsam voluptatem quia voluptas sit aspernatur aut odit aut ratione voluptatem sequi</p></article>
<article class="blog-card" style="left:790px"><p class="blog-date">OCTOBER 14, 2021</p><h3 class="blog-head">Sed ut perspiciatis unde omnis iste natus</h3><p class="blog-text">Nemo enim ipsam voluptatem quia voluptas sit aspernatur aut odit aut ratione voluptatem sequi</p></article>

<footer class="footer"></footer>
<div class="contact" style="left:118px">
  <div class="ring"><svg width="14" height="19" viewBox="0 0 10 14"><path d="M5 0a5 5 0 0 0-5 5c0 4 5 9 5 9s5-5 5-9a5 5 0 0 0-5-5zm0 7a2 2 0 1 1 0-4 2 2 0 0 1 0 4z" fill="#fff"/></svg></div>
  <h4>LOCATION</h4><p>via Fiorella Ardi 42<br>50100 Valdoro, Toscana (Italy)</p>
</div>
<div class="contact" style="left:452px">
  <div class="ring"><svg width="17" height="17" viewBox="0 0 16 16"><path d="M3.6 1 6 3.8 4.6 5.6c.9 2 3.1 4.3 5.5 5.6l1.6-1.4L14.6 12 13 15C6.5 14.5 1.5 9.6 1 3z" fill="#fff"/></svg></div>
  <h4>PHONE</h4><p>+39 055 0147 286</p>
</div>
<div class="contact" style="left:782px">
  <div class="ring"><svg width="18" height="14" viewBox="0 0 18 14"><rect width="18" height="14" rx="1.5" fill="#fff"/><path d="M1 1.5 9 8l8-6.5" fill="none" stroke="#1d1d1d" stroke-width="1.6"/></svg></div>
  <h4>EMAIL</h4><p>hello@staylune-homes.com</p>
</div>
<div class="logo" style="left:112px;top:3600px"><span class="dot"></span>StayLune</div>
<nav class="foot-nav"><a href="#">Home</a><a href="#">Last Minute</a><a href="#">Special Offers</a><a href="#">Experience</a><a href="#">Blog</a><a href="#">Contact Us</a></nav>
<p class="copyright">©2021 StayLune. All rights reserved. Privacy Policy Terms and Conditions</p>

</body>
</html>
```